Packaging Design for Vanta Core

We require an outstanding packaging design for our Vanta Core brand, which offers hydration electrolyte supplements specifically tailored for athletes and sporty individuals.

Benchmark packaging design from liquora competitor attached. The product packaging contains 20 x 20g sticks of the product.

Target Market

Psychographic: Health-conscious, active lifestyle, values quality, functionality and sustainability.

product description 1:
HYDRATION BOOSTER
Refresh, Replenish, Recharge!

product description 2:
PREMIUM ISOTONIC ELECTROLYTE DRINK
Nutritional Expertise Since 1992.

Existing Logo: to add "since 1992"

Appeal to Target Market: Create a design that resonates with both men and women in the 25-55 age group.

Grafik Design: Develop a visually striking design that grabs attention in online retail environments like Brindle.

Visuals: glass of water (or symbolic) and sticks (powder) just like benchmark brand liquora.

Design Elements
Use colours that are inside the Vanta-Core Logo, attached.
Product will be available in 3 flavours. Lemon=yellow, Orange=orange, Black Currant=purple

Typography: Utilize strong, clean, and modern fonts. Ensure readability and create a sense of strength, endurance and reliability.

The product will be available in 3 flavours: Lemon, Orange and Johannisbeere

We look forward to seeing your creative ideas and innovative designs for our Vanta Core brand packaging.

```html
<!DOCTYPE html>
<html lang="en">
<head>
<meta charset="utf-8">
<title>Vanta Core Hydration Booster – Lemon</title>
<link rel="stylesheet" href="https://fonts.googleapis.com/css2?family=Archivo+Black&family=Jost:wght@300;400;600&display=swap">
<style>
  :root {
    --stage: #2e3042;
    --navy: #272b3c;
    --lemon: #f9e11a;
    --olive: #b3a52a;
    --olive-dark: #a39626;
    --magenta: #d4146b;
    --white: #ffffff;
    --glass-tone-a: #efe6a0;
  }
  * { box-sizing: border-box; margin: 0; padding: 0; }
  html, body {
    width: 1200px; height: 848px; overflow: hidden;
    background: var(--stage);
  }
  .stage { position: relative; width: 1200px; height: 848px; }
  .pack-front {
    position: absolute;
    left: 259px; top: 44px;
    width: 1005px; height: 1120px;
    transform: scale(0.6786);
    transform-origin: 0 0;
    background: var(--lemon);
    overflow: hidden;
    box-shadow: 0 10px 30px rgba(0,0,0,.35);
  }
  .pack-shapes { position: absolute; inset: 0; }
  .count-banner {
    position: absolute; left: -88px; top: 88px;
    width: 400px; height: 44px;
    display: flex; align-items: center; justify-content: center;
    transform: rotate(-45deg); transform-origin: 50% 50%;
    font: 400 38px/1 'Jost', sans-serif; color: var(--navy);
    white-space: nowrap;
  }
  .brand {
    position: absolute; left: 135px; top: 230px;
    display: flex; align-items: center; gap: 18px;
    transform: rotate(-8deg); transform-origin: 0 50%;
  }
  .brand-dot { width: 64px; height: 64px; border-radius: 50%; background: var(--magenta); }
  .brand-name {
    font: 400 78px/1 'Archivo Black', sans-serif; color: var(--lemon);
    letter-spacing: -1px; white-space: nowrap;
  }
  .brand-since {
    position: absolute; left: 444px; top: 300px;
    transform: rotate(-8deg);
    font: 600 19px/1 'Jost', sans-serif; color: var(--white); letter-spacing: .5px;
  }
  .product-title {
    position: absolute; left: 278px; top: 440px;
    font: 400 88px/80px 'Archivo Black', sans-serif; color: var(--navy);
    letter-spacing: -2px; transform: scaleY(1.05); transform-origin: 0 0;
    white-space: nowrap;
  }
  .tagline {
    position: absolute; left: 278px; top: 612px;
    font: 400 35px/1 'Jost', sans-serif; color: var(--navy); letter-spacing: .5px;
    white-space: nowrap;
  }
  .product-type {
    position: absolute; left: 278px; top: 682px;
    font: 400 40px/38px 'Archivo Black', sans-serif; color: var(--navy);
    letter-spacing: -1px;
  }
  .heritage {
    position: absolute; left: 278px; top: 846px;
    font: 300 31px/26px 'Jost', sans-serif; color: var(--navy);
  }
  .flavour {
    position: absolute; left: 770px; top: 985px; width: 140px;
    text-align: center; color: var(--navy);
  }
  .flavour-name { font: 400 33px/1 'Archivo Black', sans-serif; }
  .flavour-count { font: 400 32px/28px 'Jost', sans-serif; margin-top: 8px; }
</style>
</head>
<body>
<main class="stage">
  <section class="pack-front" aria-label="Vanta Core Hydration Booster lemon pack front">
    <svg class="pack-shapes" viewBox="0 0 1005 1120" width="1005" height="1120">
      <path class="navy-wave" fill="var(--navy)"
        d="M0,0 H1005 V38 C880,140 780,330 520,376 C400,395 320,405 262,432 C190,475 110,600 0,655 Z"/>
      <polygon class="count-band" fill="var(--white)" points="156,0 291,0 0,291 0,158"/>
      <path class="leaf-shape" fill="var(--olive)" d="M0,820 C40,812 80,815 88,840 C110,930 120,1040 150,1120 H0 Z"/>
      <path class="leaf-shape" fill="var(--olive-dark)" d="M120,1120 C110,1010 130,880 190,840 C240,810 285,900 310,1000 C330,1070 350,1100 365,1120 Z"/>
      <rect role="img" aria-label="Lemon wedges with green leaves" x="40" y="960" width="340" height="150" rx="60" fill="var(--olive)" opacity=".55"/>
      <defs>
        <radialGradient id="glassGlow" cx="50%" cy="55%" r="60%">
          <stop offset="0" stop-color="var(--glass-tone-a)"/>
          <stop offset="1" stop-color="var(--lemon)"/>
        </radialGradient>
      </defs>
      <rect role="img" aria-label="Hydration stick pouring powder into a splashing glass of water" x="470" y="570" width="450" height="540" rx="40" fill="url(#glassGlow)"/>
    </svg>

    <div class="count-banner">20 x 20g Sticks</div>

    <div class="brand">
      <span class="brand-dot"></span>
      <span class="brand-name">Vanta Core</span>
    </div>
    <div class="brand-since">SINCE 1992</div>

    <h1 class="product-title">HYDRATION<br>BOOSTER</h1>
    <p class="tagline">Refresh, Replenish, Recharge!</p>
    <h2 class="product-type">PREMIUM<br>ISOTONIC<br>ELECTROLYTE<br>DRINK</h2>
    <p class="heritage">Nutritional Expertise<br>Since 1992.</p>

    <div class="flavour">
      <div class="flavour-name">LEMON</div>
      <div class="flavour-count">20 x 20g<br>Sticks</div>
    </div>
  </section>
</main>
</body>
</html>
```